We Are Corvale Marketing Collateral

We Are Corvale has undergone a rebrand with new logo, website, and intranet design builds. The business is now looking to update its marketing collateral with the new logo design and colour palette. Deliverables include PowerPoint template, Report template, Letterhead, and Email signature. Refer attached design brief for more information. Also attached are the logo and brand document.
Target Market(s)
Executive & Board of SME impact organisations.
Industry/Entity Type
We serve small to medium organisations who are delivering impact, not-for-profits, social enterprises and purpose driven organisations.
Font styles to use
Other font styles liked:
- Roca Two Thin, Rubik Regular
Look and feel
Each slider illustrates characteristics of the customer's brand and the style your logo design should communicate.

```html
<!DOCTYPE html>
<html lang="en">
<head>
<meta charset="utf-8">
<title>We Are Corvale — Marketing Collateral</title>
<link href="https://fonts.googleapis.com/css2?family=Fraunces:opsz,wght@9..144,300&family=Rubik:wght@300;400;500;700&display=swap" rel="stylesheet">
<style>
:root{
  --bg:#d5f1e8;
  --forest:#1b4d44;
  --sage:#a3d0c1;
  --sage-light:#d6ece4;
  --sage-dark:#5e9a86;
  --sage-mid:#93bfae;
  --sage-pale:#c4e0d5;
  --white:#ffffff;
  --ink:#1f2a28;
  --grey:#8a9592;
  --pink:#e0457b;
  --orange:#f47c4a;
  --teal:#2fa3a0;
  --green:#4cae6d;
  --blue:#3b8fc8;
  --send:#1a73e8;
  --serif:"Fraunces",Georgia,serif;
  --sans:"Rubik",Arial,sans-serif;
}
*{box-sizing:border-box;margin:0;padding:0}
html,body{width:1200px;height:1200px;overflow:hidden}
body{background:var(--bg);font-family:var(--sans);color:var(--ink);position:relative}
.abs{position:absolute}

/* brand lockup */
.brand{position:absolute;left:175px;top:32px;display:flex;align-items:center;gap:48px}
.brand-dot{width:110px;height:110px;border-radius:50%;background:var(--forest)}
.brand-name{font-family:var(--sans);font-weight:300;font-size:64px;letter-spacing:6px;color:var(--forest)}

/* mini lockup used on pieces */
.mini-brand{position:absolute;display:flex;align-items:center;gap:3px;font-family:var(--sans);font-weight:500;color:var(--white)}
.mini-brand i{display:block;border-radius:50%;background:currentColor}
.mini-brand.dark{color:var(--forest)}

/* slides */
.slide{position:absolute;width:288px;height:161px;overflow:hidden;background:var(--white);box-shadow:0 2px 6px rgba(0,0,0,.12)}
.slide.forest{background:var(--forest);color:var(--white)}
.slide.sage{background:var(--sage)}
.slide-title{position:absolute;font-family:var(--serif);font-weight:300;color:var(--forest)}
.slide-title.center{left:0;right:0;text-align:center;top:16px;font-size:15px}
.slide-url{position:absolute;right:10px;bottom:7px;font-size:4.5px;color:var(--grey)}
.corner-dot{position:absolute;left:10px;bottom:8px;width:13px;height:13px;border-radius:50%;background:var(--sage)}
.caption{position:absolute;width:288px;text-align:center;font-size:22px;font-weight:400;color:var(--forest)}

.col1{left:53px}.col2{left:413px}
.row1{top:187px}.row2{top:450px}.row3{top:717px}.row4{top:983px}
.cap1{top:355px}.cap2{top:620px}.cap3{top:886px}.cap4{top:1152px}

.deco{position:absolute}
.deco-dots{background:linear-gradient(160deg,var(--teal),var(--pink) 45%,var(--orange) 75%,var(--green));opacity:.9}
.deco-stripes{background:linear-gradient(135deg,#f6cfe0,#fbe4c8 40%,#cfe9f0 70%,#dcf0e2)}
.deco-ring{background:radial-gradient(circle,rgba(255,255,255,.55),rgba(255,255,255,0) 70%)}

/* table slide */
.data-table{position:absolute;left:18px;right:18px;top:43px;border-collapse:collapse;font-size:4.6px;color:var(--ink)}
.data-table th{background:var(--sage);color:var(--white);font-weight:500;height:15px;letter-spacing:.3px}
.data-table td{height:17px;text-align:center;border-bottom:.6px solid var(--sage)}
.data-table td,.data-table th{border-left:.6px solid var(--sage);border-right:.6px solid var(--sage)}

/* team */
.team{position:absolute;left:30px;right:30px;top:44px;display:flex;justify-content:space-between}
.member{width:48px;text-align:center}
.member .photo{width:44px;height:44px;margin:0 auto;background:linear-gradient(160deg,#e9ddd2,#b99c86)}
.member .name{margin-top:10px;font-size:4px;font-weight:500;letter-spacing:.4px;color:var(--forest)}
.member .role{margin-top:4px;font-size:3.4px;color:var(--forest);line-height:1.3}

/* flow */
.flow{position:absolute;left:20px;right:20px;top:55px;display:flex;gap:3px}
.flow-step{flex:1}
.flow-head{background:var(--sage);color:var(--white);font-size:4.2px;font-weight:500;text-align:center;height:13px;line-height:13px;letter-spacing:.4px}
.flow-body{margin-top:2px;background:var(--sage-light);height:38px;padding:4px;font-size:4.2px;line-height:1.3;color:var(--ink)}

/* report */
.report-cover{position:absolute;left:748px;top:36px;width:215px;height:303px;background:var(--forest);box-shadow:0 3px 8px rgba(0,0,0,.2);z-index:3;overflow:hidden}
.report-title{position:absolute;left:16px;top:128px;font-family:var(--serif);font-weight:300;font-size:27px;line-height:1.1;color:var(--white)}
.report-sub{position:absolute;left:17px;top:200px;font-size:9px;color:var(--white)}
.page{position:absolute;width:213px;height:303px;background:var(--white);box-shadow:0 2px 6px rgba(0,0,0,.15);overflow:hidden;font-size:4px;color:var(--ink)}
.page p{position:absolute;line-height:1.4}
.page-foot{position:absolute;left:14px;bottom:14px;font-size:4px;color:var(--ink)}
.page-foot b{color:var(--forest)}
.page-num{position:absolute;right:14px;bottom:14px;font-size:4px}
.page-dot{position:absolute;right:14px;top:12px;width:9px;height:9px;border-radius:50%;background:var(--sage)}

/* letterhead */
.letter{position:absolute;left:796px;top:498px;width:285px;height:402px;background:var(--white);box-shadow:0 2px 8px rgba(0,0,0,.15);font-size:4.6px;line-height:1.45;color:var(--ink);overflow:hidden}
.letter p{position:absolute;left:36px;right:26px}
.letter-contact{position:absolute;right:26px;top:18px;text-align:right;color:var(--forest);font-size:5px;line-height:1.4}
.letter-band{position:absolute;left:0;right:0;bottom:0;height:6px;background:var(--forest)}

/* email */
.email{position:absolute;left:808px;top:967px;width:265px;height:191px;background:var(--white);box-shadow:0 2px 8px rgba(0,0,0,.18);font-size:5px;color:var(--ink);overflow:hidden}
.email-bar{height:14px;background:#eef1f0;display:flex;align-items:center;justify-content:space-between;padding:0 6px;font-size:5.5px;font-weight:500;color:var(--ink)}
.email-subject{padding:6px 6px;border-bottom:.6px solid #e1e5e4;color:#555;font-size:5px}
.email-send{position:absolute;left:6px;bottom:10px;width:42px;height:14px;border-radius:7px;background:var(--send);color:var(--white);font-size:5.5px;font-weight:500;line-height:14px;padding-left:8px}
</style>
</head>
<body>

<div class="brand">
  <div class="brand-dot"></div>
  <div class="brand-name">CORVALE</div>
</div>

<!-- Cover slide -->
<section class="slide forest col1 row1">
  <div class="mini-brand" style="left:28px;top:18px;font-size:6.5px"><i style="width:9px;height:9px"></i>CORVALE</div>
  <div class="slide-title" style="left:28px;top:54px;font-size:17px;line-height:1.15;color:var(--white)">Multi-line title<br>goes here</div>
  <div class="abs" style="left:28px;top:99px;font-size:7.5px">Subtitle or presenter name(s)</div>
  <div class="deco deco-dots" role="img" aria-label="Cluster of colourful brand dots" style="right:0;top:0;width:95px;height:161px;border-radius:60px 0 0 60px"></div>
</section>
<div class="caption col1 cap1">Cover</div>

<!-- Standard text -->
<section class="slide col2 row1">
  <div class="slide-title" style="left:32px;top:27px;font-size:14px">This is an example</div>
  <div class="abs" style="left:32px;top:63px;width:140px;font-size:5.6px;font-weight:700;line-height:1.4;color:var(--ink)">Lorem ipsum dolor sit amet, consectetur adipiscing elit. Nam tempor iaculis augue finibus fringilla. Fusce auctor sit amet nisi ac bibendum. Sed volutpat ipsum eu est interdum, a euismod lorem rutrum.</div>
  <div class="deco deco-stripes" role="img" aria-label="Pastel diagonal stripes with soft dots" style="right:0;top:0;width:110px;height:161px"></div>
  <div class="corner-dot"></div>
  <div class="slide-url">wearecorvale.com.au</div>
</section>
<div class="caption col2 cap1">Standard text</div>

<!-- Section break -->
<section class="slide sage col1 row2">
  <div class="deco deco-ring" role="img" aria-label="Faint ring of light dots" style="left:18px;top:28px;width:100px;height:100px"></div>
  <div class="slide-title" style="left:146px;top:62px;font-size:13px;color:var(--white)">Section title</div>
  <div class="abs" style="left:146px;top:82px;font-size:5px;color:var(--white)">Click to add a subtitle along here</div>
  <div class="slide-url" style="color:var(--white)">wearecorvale.com.au</div>
</section>
<div class="caption col1 cap2">Section break</div>

<!-- Chart -->
<section class="slide col2 row2">
  <div class="slide-title center">Example chart</div>
  <svg class="abs" style="left:20px;top:40px" width="250" height="100" viewBox="0 0 250 100">
    <g stroke="#e3e8e6" stroke-width=".6">
      <line x1="14" y1="10" x2="245" y2="10"/><line x1="14" y1="22" x2="245" y2="22"/>
      <line x1="14" y1="34" x2="245" y2="34"/><line x1="14" y1="46" x2="245" y2="46"/>
      <line x1="14" y1="58" x2="245" y2="58"/><line x1="14" y1="70" x2="245" y2="70"/>
    </g>
    <g font-size="4" fill="#8a9592" font-family="Rubik, sans-serif">
      <text x="6" y="12">5</text><text x="6" y="24">4</text><text x="6" y="36">3</text>
      <text x="6" y="48">2</text><text x="6" y="60">1</text><text x="6" y="72">0</text>
      <text x="36" y="78">Q1</text><text x="92" y="78">Q2</text><text x="148" y="78">Q3</text><text x="198" y="78">Category 4</text>
    </g>
    <g>
      <rect x="24" y="18.4" width="9" height="51.6" fill="#5e9a86"/><rect x="36" y="41.2" width="9" height="28.8" fill="#93bfae"/><rect x="48" y="46" width="9" height="24" fill="#c4e0d5"/>
      <rect x="80" y="40" width="9" height="30" fill="#5e9a86"/><rect x="92" y="17.2" width="9" height="52.8" fill="#93bfae"/><rect x="104" y="48.4" width="9" height="21.6" fill="#c4e0d5"/>
      <rect x="136" y="28" width="9" height="42" fill="#5e9a86"/><rect x="148" y="48.4" width="9" height="21.6" fill="#93bfae"/><rect x="160" y="34" width="9" height="36" fill="#c4e0d5"/>
      <rect x="192" y="16" width="9" height="54" fill="#5e9a86"/><rect x="204" y="36.4" width="9" height="33.6" fill="#93bfae"/><rect x="216" y="10" width="9" height="60" fill="#c4e0d5"/>
    </g>
    <g font-size="3.6" fill="#8a9592" font-family="Rubik, sans-serif">
      <rect x="90" y="84" width="3" height="3" fill="#5e9a86"/><text x="95" y="87">Series 1</text>
      <rect x="114" y="84" width="3" height="3" fill="#93bfae"/><text x="119" y="87">Series 2</text>
      <rect x="138" y="84" width="3" height="3" fill="#c4e0d5"/><text x="143" y="87">Series 3</text>
    </g>
  </svg>
  <div class="corner-dot"></div>
  <div class="slide-url">wearecorvale.com.au</div>
</section>
<div class="caption col2 cap2">Chart</div>

<!-- Table -->
<section class="slide col1 row3">
  <div class="slide-title center">Example table</div>
  <table class="data-table">
    <tr><th></th><th>CATEGORY 1</th><th>CATEGORY 2</th><th>CATEGORY 3</th><th>CATEGORY 4</th></tr>
    <tr><td>Q1</td><td>4.5</td><td>2.5</td><td>1.7</td><td>3.8</td></tr>
    <tr><td>Q2</td><td>3.2</td><td>5.1</td><td>4.4</td><td>3.8</td></tr>
    <tr><td>Q3</td><td>3.1</td><td>1.7</td><td>2.3</td><td>3.9</td></tr>
    <tr><td>Q4</td><td>4.3</td><td>2.2</td><td>1.7</td><td>7.9</td></tr>
  </table>
  <div class="corner-dot"></div>
  <div class="slide-url">wearecorvale.com.au</div>
</section>
<div class="caption col1 cap3">Table</div>

<!-- Team gallery -->
<section class="slide sage col2 row3">
  <div class="slide-title center" style="color:var(--forest)">Meet our team</div>
  <div class="team">
    <div class="member"><div class="photo" role="img" aria-label="Portrait photo of team member"></div><div class="name">SAM ELLERY</div><div class="role">President</div></div>
    <div class="member"><div class="photo" role="img" aria-label="Portrait photo of team member"></div><div class="name">ROSA TINDALL</div><div class="role">Chief Executive<br>Officer</div></div>
    <div class="member"><div class="photo" role="img" aria-label="Portrait photo of team member"></div><div class="name">MIA OKAFOR</div><div class="role">Chief Operations<br>Officer</div></div>
    <div class="member"><div class="photo" role="img" aria-label="Portrait photo of team member"></div><div class="name">LEV HARTMANN</div><div class="role">VP Marketing</div></div>
  </div>
  <div class="slide-url" style="color:var(--white)">wearecorvale.com.au</div>
</section>
<div class="caption col2 cap3">Team gallery</div>

<!-- Flowchart -->
<section class="slide col1 row4">
  <div class="slide-title center" style="top:20px">Example flowchart</div>
  <div class="flow">
    <div class="flow-step"><div class="flow-head">PLANNING</div><div class="flow-body">Synergize scalable e-commerce</div></div>
    <div class="flow-step"><div class="flow-head">MARKETING</div><div class="flow-body">Disseminate standardized metrics</div></div>
    <div class="flow-step"><div class="flow-head">DESIGN</div><div class="flow-body">Coordinate e-business applications</div></div>
    <div class="flow-step"><div class="flow-head">STRATEGY</div><div class="flow-body">Foster holistically superior methodologies</div></div>
    <div class="flow-step"><div class="flow-head">LAUNCH</div><div class="flow-body">Deploy strategic networks with compelling e-business needs</div></div>
  </div>
  <div class="corner-dot"></div>
  <div class="slide-url">wearecorvale.com.au</div>
</section>
<div class="caption col1 cap4">Flowchart</div>

<!-- Closing -->
<section class="slide forest col2 row4">
  <div class="deco deco-dots" role="img" aria-label="Cluster of colourful brand dots" style="left:0;top:0;width:110px;height:161px;border-radius:0 70px 70px 0"></div>
  <div class="slide-title" style="right:22px;top:58px;font-size:14px;color:var(--white)">Closing slide</div>
  <div class="abs" style="right:22px;top:84px;text-align:right;font-size:5.8px;line-height:1.55">Your Name<br>yourname@corvale.com<br>wearecorvale.com.au</div>
  <div class="mini-brand" style="right:22px;bottom:12px;font-size:7px"><i style="width:9px;height:9px"></i>CORVALE</div>
</section>
<div class="caption col2 cap4">Closing</div>

<!-- Report pages -->
<div class="page" style="left:942px;top:131px;z-index:1">
  <div class="page-dot"></div>
  <p style="left:100px;top:18px;width:100px">Lorem ipsum dolor sit amet and start typing here</p>
  <p style="left:100px;top:34px;width:100px">Add text, box, or table? You got it! On the</p>
  <svg class="abs" style="left:100px;top:48px" width="100" height="40" viewBox="0 0 100 40">
    <rect x="0" y="0" width="100" height="6" fill="#a3d0c1"/>
    <g stroke="#a3d0c1" stroke-width=".5" fill="none"><rect x="0" y="0" width="100" height="38"/><line x1="0" y1="14" x2="100" y2="14"/><line x1="0" y1="22" x2="100" y2="22"/><line x1="0" y1="30" x2="100" y2="30"/><line x1="50" y1="0" x2="50" y2="38"/></g>
  </svg>
  <p style="left:100px;top:92px;width:100px">Lorem ipsum dolor sit and start typing here</p>
  <p style="left:100px;top:108px;width:100px">Add text, box, or table? You got it! On the</p>
  <div class="page-foot"><b>We Are Corvale</b> | Annual Report 2022</div>
  <div class="page-num">3</div>
</div>
<div class="page" style="left:848px;top:76px;z-index:2">
  <div class="page-dot"></div>
  <p style="left:120px;top:42px;width:80px">Lorem ipsum dolor sit amet and start typing</p>
  <p style="left:120px;top:62px;width:80px">Add text, box, or table? You got it!</p>
  <div class="abs" style="left:120px;top:88px;width:84px;height:26px;background:var(--sage-light)"></div>
  <p style="left:120px;top:126px;width:80px">Lorem ipsum dolor sit amet and start typing</p>
  <svg class="abs" style="left:120px;top:146px" width="84" height="46" viewBox="0 0 84 46">
    <rect x="0" y="0" width="84" height="46" fill="none" stroke="#e3e8e6" stroke-width=".5"/>
    <rect x="8" y="14" width="5" height="26" fill="#5e9a86"/><rect x="14" y="22" width="5" height="18" fill="#93bfae"/>
    <rect x="48" y="10" width="5" height="30" fill="#5e9a86"/><rect x="54" y="20" width="5" height="20" fill="#93bfae"/><rect x="60" y="6" width="5" height="34" fill="#c4e0d5"/>
  </svg>
  <p style="left:120px;top:208px;width:80px">Add text, box, or table? You got it! On the tab of the ribbon, pick the option you need.</p>
  <div class="page-foot"><b>We Are Corvale</b> | Annual Report 2022</div>
  <div class="page-num">2</div>
</div>

<!-- Report cover -->
<div class="report-cover">
  <div class="deco deco-dots" role="img" aria-label="Cascade of colourful brand dots" style="left:0;top:0;width:215px;height:115px;border-radius:0 0 90px 90px"></div>
  <div class="report-title">Annual Report<br>2022</div>
  <div class="report-sub">Editor or Subtitle Text</div>
  <div class="mini-brand" style="left:0;right:0;justify-content:center;bottom:14px;font-size:9px"><i style="width:11px;height:11px"></i>CORVALE</div>
</div>

<!-- Letterhead -->
<div class="letter">
  <div class="mini-brand dark" style="left:34px;top:20px;font-size:10px;gap:5px"><i style="width:14px;height:14px"></i>CORVALE</div>
  <div class="letter-contact">+61 400 000 111<br>name@email.com<br>wearecorvale.com.au</div>
  <p style="top:58px;left:auto;right:26px;text-align:right">9 November 2022</p>
  <p style="top:68px;font-weight:700">RE: Client meeting – feedback and next steps</p>
  <p style="top:86px">Dear Sir/Madam,</p>
  <p style="top:98px">Lorem ipsum dolor sit amet, consectetur adipiscing elit. Cras at eros quis nisl luctus posuere sit amet sit amet magna. Quisque mollis dignissim justo, et efficitur orci iaculis eget. Aenean porta tellus et ex dignissim aliquet. Pellentesque maximus eget ex sit amet accumsan. Pellentesque habitant morbi tristique senectus et netus et malesuada fames ac turpis egestas.</p>
  <p style="top:140px">Duis quis mauris erat. Maecenas rhoncus ex non mi iaculis elementum. Integer pharetra eu tellus at finibus. Donec bibendum justo turpis, at luctus lectus imperdiet ut. Maecenas sed dignissim ipsum. Nunc felis urna, mattis non imperdiet in, consequat sit amet purus.</p>
  <p style="top:175px">Nunc porttitor id tellus eu dictum. Fusce lacus metus, sollicitudin sed diam vitae, sagittis pulvinar erat. In bibendum cursus maximus. In laoreet velit a nisi efficitur viverra. Nunc ac urna molestie ex molestie lacinia. Sed vel sollicitudin lectus. Nullam sodales sit amet erat ac semper.</p>
  <p style="top:210px">Class aptent taciti sociosqu ad litora torquent per conubia nostra, per inceptos himenaeos. Ut porttitor venenatis tortor.</p>
  <p style="top:228px">Donec dui turpis, cursus finibus bibendum eu, ultricies ac tellus. Sed finibus nulla auctor, tempor sem sed, lacinia est. Suspendisse sed nunc suscipit, malesuada urna nec, fringilla nisi. Aliquam in diam neque.</p>
  <p style="top:256px">Sed suscipit est in ultrices mattis. Ut leo magna, interdum et elit non, bibendum convallis augue. Vivamus est eros, sollicitudin a nisi quis, ornare fringilla dui.</p>
  <p style="top:288px">Kind regards,</p>
  <div class="abs" role="img" aria-label="Handwritten signature" style="left:36px;top:298px;width:44px;height:14px;background:linear-gradient(90deg,#e8ecea,#f6f8f7)"></div>
  <p style="top:318px;font-weight:700;color:var(--forest)">Dana Whitlock</p>
  <p style="top:328px">Director &amp; CFO<br>We Are Corvale</p>
  <div class="abs" style="left:138px;top:380px;width:9px;height:9px;border-radius:50%;background:var(--sage-light)"></div>
  <div class="letter-band"></div>
</div>

<!-- Email signature -->
<div class="email">
  <div class="email-bar"><span>We Are Corvale Email Signature</span><span style="letter-spacing:3px">– ⤢ ✕</span></div>
  <div class="email-subject">We Are Corvale Email Signature</div>
  <div class="abs" style="left:6px;top:44px;line-height:1.5">This is an example email<br><br>Kind regards,</div>
  <div class="abs" style="left:6px;top:78px;line-height:1.5">
    <div style="font-weight:700;font-size:6px;color:var(--forest)">Dana Whitlock</div>
    <div>Director &amp; CFO</div>
    <div>We Are Corvale</div>
  </div>
  <div class="abs" style="left:76px;top:80px;width:.6px;height:30px;background:#b9c4c1"></div>
  <svg class="abs" style="left:84px;top:80px" width="8" height="30" viewBox="0 0 8 30" fill="var(--ink)">
    <path d="M1.5 1c.5-.5 1.2-.3 1.5.2l.8 1.3c.2.4.1.9-.2 1.1l-.5.4c.3.8.9 1.4 1.6 1.7l.4-.5c.3-.3.7-.4 1.1-.2l1.3.8c.5.3.6 1 .2 1.4C6.6 8.5 5 8.2 3.3 6.5S.9 2.9 1.5 1z"/>
    <rect x="1" y="13" width="6" height="4" rx=".5"/>
    <rect x="1.5" y="23" width="5" height="5" rx=".6" fill="none" stroke="var(--ink)" stroke-width=".7"/>
  </svg>
  <div class="abs" style="left:98px;top:80px;line-height:2.05">+61 400 000 111<br>name@email.com<br>wearecorvale.com.au</div>
  <div class="abs" style="left:6px;top:120px;width:130px;height:.6px;background:#b9c4c1"></div>
  <div class="mini-brand dark" style="left:6px;top:138px;font-size:6px"><i style="width:8px;height:8px"></i>CORVALE</div>
  <div class="abs" style="left:116px;top:136px;width:10px;height:10px;border-radius:50%;background:var(--forest)"></div>
  <div class="email-send">Send ▾</div>
  <svg class="abs" style="left:56px;bottom:13px" width="120" height="8" viewBox="0 0 120 8" fill="none" stroke="#5f6368" stroke-width=".7">
    <text x="0" y="6.5" font-size="7" fill="#5f6368" stroke="none" font-family="Rubik, sans-serif">A</text>
    <path d="M14 1v5M12 4l2 2 2-2"/><path d="M24 4h6M27 2l2 2-2 2"/><circle cx="37" cy="4" r="3"/>
    <path d="M46 1l3 3-3 3M49 4h-4"/><rect x="55" y="1" width="6" height="6"/><path d="M68 1v6l2-1.5L72 7V1z"/>
    <circle cx="80" cy="2" r=".6"/><circle cx="80" cy="4" r=".6"/><circle cx="80" cy="6" r=".6"/>
  </svg>
  <svg class="abs" style="right:8px;bottom:13px" width="7" height="8" viewBox="0 0 7 8" fill="none" stroke="#5f6368" stroke-width=".7"><path d="M1 2h5M2.5 2V1h2v1M1.5 2l.5 5.5h3L5.5 2"/></svg>
</div>

</body>
</html>
```